2022 Landscaping Services

Please use the prior year design as an example. Similar style but DO NOT COPY IT EXACTLY- you can use different photos from our website if you like. Same text for year 2022.
Design should clearly depict the differences between the 3 products so people can buy one of them. Be creative!

size 8.5" x 11"

Must provide source file in photoshop if you are winner

Requirements
Must have
• Same text as original flier but with year 2022

```html
<!DOCTYPE html>
<html lang="en">
<head>
<meta charset="utf-8">
<title>2022 Gravesite Landscaping Packages</title>
<link rel="stylesheet" href="https://fonts.googleapis.com/css2?family=Poppins:wght@400;500;600;700;800&display=swap">
<style>
:root{
  --red:#8e1a1d;
  --red-deep:#6d1215;
  --black:#161616;
  --ink:#1c1c1c;
  --grey-band:#e4dfdf;
  --bg:#e9e9e9;
  --gold:#e0a81c;
  --tick:#2e9a3a;
  --ban:#c8202a;
  --white:#ffffff;
  --muted:#555555;
}
*{margin:0;padding:0;box-sizing:border-box}
html,body{width:1200px;height:2171px;overflow:hidden;background:var(--bg);font-family:"Poppins",sans-serif}
.flyer{position:absolute;left:0;top:309px;width:860px;height:1113px;background:var(--white);overflow:hidden;transform:scale(1.3953);transform-origin:0 0}
.abs{position:absolute}
.brand{left:58px;top:52px;display:flex;align-items:center;gap:10px;color:var(--red);font-weight:500;font-size:22px;letter-spacing:.5px}
.brand-dot{width:16px;height:16px;border-radius:50%;background:var(--red)}
.year-band{left:0;top:128px;width:560px;height:127px;background:var(--black)}
.year{left:58px;top:140px;color:var(--white);font-weight:800;font-size:112px;line-height:1;letter-spacing:-2px}
.title-band{left:0;top:255px;width:560px;height:181px;background:var(--grey-band)}
.title{left:58px;top:272px;font-weight:800;font-size:45px;line-height:50px;letter-spacing:-.5px}
.title .dark{color:var(--ink)}
.title .red{color:var(--red)}
.photo{left:0;top:0}
.services{left:58px;top:470px;color:var(--red);font-weight:700;font-size:37px;line-height:46px}
.labels{left:58px;top:576px;width:200px}
.label{display:flex;align-items:center;padding-left:11px;font-size:11.5px;font-weight:600;line-height:15px;color:var(--ink);text-transform:uppercase}
.label.alt{background:var(--red);color:var(--white)}
.col{top:436px;width:180px}
.col-head{height:140px;background:linear-gradient(160deg,#2b2b2b,#0d0d0d);color:var(--white);text-align:center;font-weight:600;font-size:19px;line-height:21px;display:flex;flex-direction:column;justify-content:center;padding-top:30px}
.col.pop .col-head{background:linear-gradient(160deg,#a1232a,var(--red-deep))}
.col-desc{height:50px;font-size:9px;line-height:11.5px;color:var(--muted);padding:8px 0 0 22px;border-bottom:2px solid var(--black)}
.col.pop .col-desc{border-color:var(--red)}
.cell{display:flex;align-items:center;justify-content:center;background:linear-gradient(90deg,#ffffff 55%,#e9e9e9);border-bottom:2px solid var(--black)}
.col.pop .cell{border-color:var(--red)}
.cell svg{width:19px;height:19px}
.price{height:43px;color:var(--white);text-align:center;font-weight:600;font-size:20px;line-height:43px;background:linear-gradient(90deg,#0f0f0f,#2a2a2a)}
.price.multi{font-size:15px;line-height:18px;padding-top:4px}
.price.multi small{display:block;font-size:10.5px;font-weight:500;line-height:14px}
.col.pop .price{background:linear-gradient(90deg,var(--red-deep),#a1232a)}
.note{font-size:11px;line-height:14px;color:var(--ink);font-weight:500;padding:10px 0 0 10px}
.tag{left:611px;top:456px;width:195px;height:24px;background:var(--gold);color:var(--black);font-weight:700;font-size:15px;line-height:24px;text-align:center}
.valid{left:73px;top:906px;width:150px;height:72px;border:2px solid var(--black);border-top:none;border-bottom:none}
.valid-tag{position:absolute;left:14px;top:0;width:118px;background:var(--red);color:var(--white);font-weight:600;font-size:19px;line-height:19px;text-align:center;padding:3px 0}
.valid-date{position:absolute;left:0;right:0;top:44px;text-align:center;font-weight:700;font-size:26px;line-height:28px;color:var(--black)}
.footer{left:0;top:1046px;width:860px;height:67px;display:grid;grid-template-columns:278px 303px 279px;color:var(--white)}
.footer div{display:flex;align-items:center;justify-content:center;text-align:center;font-size:13px;font-weight:500;line-height:17px;background:var(--black)}
.footer .phone{background:var(--red);font-size:24px;font-weight:600}
.icon-dot{width:38px;height:38px;border-radius:50%;background:var(--black);border:2px solid var(--white);display:flex;align-items:center;justify-content:center}
.icon-dot svg{width:20px;height:20px}
</style>
</head>
<body>
<svg width="0" height="0" style="position:absolute">
  <defs>
    <symbol id="ban" viewBox="0 0 20 20"><circle cx="10" cy="10" r="8" fill="none" stroke="#c8202a" stroke-width="2"/><line x1="4.5" y1="4.5" x2="15.5" y2="15.5" stroke="#c8202a" stroke-width="2"/></symbol>
    <symbol id="tick" viewBox="0 0 20 20"><circle cx="10" cy="10" r="8" fill="none" stroke="#2e9a3a" stroke-width="1.6"/><path d="M6 10.3l2.7 2.7L14.2 7.4" fill="none" stroke="#2e9a3a" stroke-width="1.8" stroke-linecap="round" stroke-linejoin="round"/></symbol>
  </defs>
</svg>

<div class="flyer">
  <div class="abs brand"><span>Willowbrook Cemetery</span><span class="brand-dot"></span></div>

  <div class="abs year-band"></div>
  <div class="abs title-band"></div>

  <svg class="abs photo" width="860" height="1113" viewBox="0 0 860 1113">
    <defs>
      <linearGradient id="scene" x1="0" y1="0" x2="0" y2="1">
        <stop offset="0" stop-color="#6f7d5e"/>
        <stop offset=".45" stop-color="#9aa58d"/>
        <stop offset=".7" stop-color="#4f6b35"/>
        <stop offset="1" stop-color="#3d5a26"/>
      </linearGradient>
    </defs>
    <circle cx="735" cy="130" r="310" fill="url(#scene)" role="img" aria-label="Photo of a young deer standing among headstones and hedges in the cemetery grounds"/>
    <path d="M626 -169 A318 318 0 0 0 576 405" fill="none" stroke="#161616" stroke-width="6"/>
    <path d="M412 187 A328 328 0 0 0 899 414" fill="none" stroke="#8e1a1d" stroke-width="6"/>
  </svg>

  <div class="abs year">2022</div>
  <div class="abs title">
    <div class="dark">GRAVESITE</div>
    <div class="red">LANDSCAPING</div>
    <div class="red">PACKAGES</div>
  </div>

  <div class="abs services">Services<br>Offered</div>

  <div class="abs labels">
    <div class="label" style="height:50px">Weeding &amp; trimming on<br>your gravesite</div>
    <div class="label alt" style="height:45px">Payment ensured<br>forever grave care</div>
    <div class="label" style="height:42px">Monument leveling</div>
    <div class="label alt" style="height:45px">Monument cleaning</div>
    <div class="label" style="height:48px">Full bed of boxwood<br>shrubs</div>
    <div class="label alt" style="height:45px">Replacement of shrubs</div>
    <div class="label" style="height:45px">Trust certificate</div>
  </div>

  <div class="abs col" style="left:258px">
    <div class="col-head">SEASONAL<br>CARE<br>ENDOWMENT</div>
    <div class="col-desc">Approximately every 7 weeks<br>during the growing season:<br>Mid-April through Mid-October</div>
    <div class="cell" style="height:45px"><svg><use href="#ban"/></svg></div>
    <div class="cell" style="height:42px"><svg><use href="#ban"/></svg></div>
    <div class="cell" style="height:45px"><svg><use href="#ban"/></svg></div>
    <div class="cell" style="height:48px"><svg><use href="#ban"/></svg></div>
    <div class="cell" style="height:45px"><svg><use href="#ban"/></svg></div>
    <div class="cell" style="height:45px;border-bottom:none"><svg><use href="#ban"/></svg></div>
    <div class="price multi">$357 | $238 | $119<small>3 Years 2 Years 1 Year</small></div>
    <div class="note">Multi-year payment locks<br>in current rates</div>
  </div>

  <div class="abs col" style="left:440px;width:178px">
    <div class="col-head">BASIC<br>CARE<br>ENDOWMENT</div>
    <div class="col-desc">2 times per year:<br>Mid-May and Mid-September</div>
    <div class="cell" style="height:45px"><svg><use href="#tick"/></svg></div>
    <div class="cell" style="height:42px"><svg><use href="#tick"/></svg></div>
    <div class="cell" style="height:45px"><svg><use href="#ban"/></svg></div>
    <div class="cell" style="height:48px"><svg><use href="#ban"/></svg></div>
    <div class="cell" style="height:45px"><svg><use href="#ban"/></svg></div>
    <div class="cell" style="height:45px;border-bottom:none"><svg><use href="#ban"/></svg></div>
    <div class="price">$255</div>
    <div class="note" style="padding-left:18px">12 Monthly payments.<br>Call for single payment<br>discounts.</div>
  </div>

  <div class="abs col pop" style="left:618px;width:181px">
    <div class="col-head">PERPETUAL<br>CARE<br>ENDOWMENT</div>
    <div class="col-desc">Approximately every 7 weeks<br>during the growing season:<br>Mid-April through Mid-October</div>
    <div class="cell" style="height:45px"><svg><use href="#tick"/></svg></div>
    <div class="cell" style="height:42px"><svg><use href="#tick"/></svg></div>
    <div class="cell" style="height:45px"><svg><use href="#tick"/></svg></div>
    <div class="cell" style="height:48px"><svg><use href="#tick"/></svg></div>
    <div class="cell" style="height:45px"><svg><use href="#tick"/></svg></div>
    <div class="cell" style="height:45px;border-bottom:none"><svg><use href="#tick"/></svg></div>
    <div class="price">$313</div>
    <div class="note" style="padding-left:14px">12 Monthly payments.<br>Call for single payment<br>discounts.</div>
  </div>

  <div class="abs tag">MOST POPULAR</div>

  <div class="abs valid">
    <div class="valid-tag">VALID<br>THROUGH</div>
    <div class="valid-date">10/31/21</div>
  </div>

  <div class="abs footer">
    <div>48 Orchard Lane Maple<br>Glen NJ 07990</div>
    <div class="phone">(555) 014-2290</div>
    <div>willowbrookcemetery.org</div>
  </div>

  <div class="abs icon-dot" style="left:101px;top:1020px">
    <svg viewBox="0 0 20 20"><path d="M10 2.5a5 5 0 0 0-5 5c0 3.8 5 9.5 5 9.5s5-5.7 5-9.5a5 5 0 0 0-5-5z" fill="none" stroke="#fff" stroke-width="1.6"/><circle cx="10" cy="7.5" r="1.8" fill="#fff"/></svg>
  </div>
  <div class="abs icon-dot" style="left:407px;top:1020px">
    <svg viewBox="0 0 20 20"><path d="M5.5 3h3l1.3 3.5-1.9 1.3a8 8 0 0 0 4.3 4.3l1.3-1.9 3.5 1.3v3a1.5 1.5 0 0 1-1.6 1.5A13 13 0 0 1 4 4.6 1.5 1.5 0 0 1 5.5 3z" fill="#fff"/></svg>
  </div>
  <div class="abs icon-dot" style="left:695px;top:1020px">
    <svg viewBox="0 0 20 20"><circle cx="10" cy="10" r="7" fill="none" stroke="#fff" stroke-width="1.5"/><ellipse cx="10" cy="10" rx="3" ry="7" fill="none" stroke="#fff" stroke-width="1.3"/><line x1="3" y1="10" x2="17" y2="10" stroke="#fff" stroke-width="1.3"/></svg>
  </div>
</div>
</body>
</html>
```